Business Cards for Bramblewood Coatings Pty Ltd

Hi every one i need a design for my buisness cards. I Want my logo in it and the name of the company needs to stand out Bramblewood Coatings Pty Ltd. I want the background of the buisness cards black and i want the font to stand out in either a white or a silver stylish text. I want the design to be simple but original not to in your face if you know what i mean. I want on the back of the buisness cards to have the services that my buisness offers.
• Interior/Exterior
• Residential/Commercial
• Special effects/Texture Coatings
• Water Damage Repair
• Fully qualified
• Pensioner Discount
• 10 Year guarantee
• Fully Insured
• Obligation free quotes
full internal repaints include a proffesionla cleaning service
I want the services on the back to be layed out in an originall way not just dot points. If possible could my logo take up the whole back ground of the back but the text with the services be kind of like transparent so u cvan still see the logo i dont know if its possible it woiuld just look cool if possible. When i pick a design ill give my contact details to the designer to add to the design at the end. Any questions please just ask! Ill upload my logo.
Conatcs will include office phone: Mobile: E-mail - dean@bramblewoodcoatings.com.au, Ill also have a Postal address which is a PO Box and my website is www.bramblewoodcoatings.com.au

```html
<!DOCTYPE html>
<html lang="en">
<head>
<meta charset="utf-8">
<title>Bramblewood Coatings Pty Ltd — Business Cards</title>
<link href="https://fonts.googleapis.com/css2?family=Arimo:wght@400;700&display=swap" rel="stylesheet">
<style>
  :root {
    --page: #e9e6e1;
    --card: #0b0b0b;
    --green: #8dc63f;
    --white: #f2f2f2;
    --silver: #d4d4d4;
    --rule: #4a4a4a;
  }
  * { margin: 0; padding: 0; box-sizing: border-box; }
  html, body {
    width: 1200px; height: 1200px; overflow: hidden;
    background: var(--page);
    font-family: "Arimo", Arial, sans-serif;
  }
  .canvas { position: relative; width: 1200px; height: 1200px; }
  .card {
    position: absolute; left: 192px; width: 816px; height: 460px;
    background: var(--card);
    box-shadow: 0 6px 18px rgba(0,0,0,0.25);
    overflow: hidden;
  }
  .card--front { top: 150px; }
  .card--back { top: 624px; }

  .brand { position: absolute; text-align: center; }
  .brand__mark {
    display: block; width: 140px; height: 136px; margin: 0 auto;
    background: var(--green); border-radius: 8px;
  }
  .brand__name {
    margin-top: 34px; color: var(--silver);
    font-weight: 700; font-size: 26px; line-height: 1; letter-spacing: 0.2px;
    white-space: nowrap;
  }
  .brand__suffix {
    margin-top: 14px; color: var(--green);
    font-weight: 700; font-size: 24px; line-height: 1;
  }
  .card--front .brand { left: 50px; top: 94px; width: 380px; }
  .card--back .brand { left: 36px; top: 96px; width: 380px; }

  .contact {
    position: absolute; right: 50px; top: 90px; text-align: right;
    color: var(--white); font-size: 17px; line-height: 1.4;
  }
  .contact__name { font-size: 26px; letter-spacing: 0.5px; line-height: 1.1; }
  .contact__role { color: var(--green); font-weight: 700; font-size: 20px; margin-top: 4px; }
  .contact__postal { margin-top: 34px; line-height: 1.5; }
  .contact__lines { margin-top: 24px; line-height: 1.35; }
  .contact__label { color: var(--green); }

  .accent-bar {
    position: absolute; left: 0; right: 0; top: 430px; height: 16px;
    display: flex;
  }
  .accent-bar__green { width: 500px; background: var(--green); }
  .accent-bar__silver {
    flex: 1;
    background: linear-gradient(90deg, #f4f4f4 0%, #bdbdbd 45%, #6f6f6f 100%);
  }

  .divider {
    position: absolute; left: 440px; top: 66px; width: 0; height: 320px;
    border-left: 2px dotted var(--rule);
  }
  .services {
    position: absolute; left: 464px; top: 96px; list-style: none;
    font-size: 19px; line-height: 30.6px;
  }
  .services li::before { content: "\2022"; margin-right: 8px; }
  .services li:nth-child(odd) { color: var(--green); }
  .services li:nth-child(even) { color: var(--white); }
</style>
</head>
<body>
<div class="canvas">
  <section class="card card--front">
    <div class="brand">
      <span class="brand__mark"></span>
      <p class="brand__name">BRAMBLEWOOD COATINGS</p>
      <p class="brand__suffix">PTY LTD</p>
    </div>
    <div class="contact">
      <p class="contact__name">DEAN HARROW</p>
      <p class="contact__role">President &amp; CEO</p>
      <p class="contact__postal">PO. BOX 4821 555 019<br>Kestrel Bay NSW</p>
      <p class="contact__lines">
        <span class="contact__label">Office.</span> (02) 5550 1824<br>
        <span class="contact__label">Mobile.</span> 0400 555 318<br>
        dean@bramblewoodcoatings.com.au<br>
        www.bramblewoodcoatings.com.au
      </p>
    </div>
    <div class="accent-bar">
      <span class="accent-bar__green"></span>
      <span class="accent-bar__silver"></span>
    </div>
  </section>

  <section class="card card--back">
    <div class="brand">
      <span class="brand__mark"></span>
      <p class="brand__name">BRAMBLEWOOD COATINGS</p>
      <p class="brand__suffix">PTY LTD</p>
    </div>
    <span class="divider"></span>
    <ul class="services">
      <li>Interior/Exterior</li>
      <li>Residential/Commercial</li>
      <li>Special effects/Texture Coatings</li>
      <li>Water Damage Repair</li>
      <li>Fully qualified</li>
      <li>Pensioner Discount</li>
      <li>10 Year guarantee</li>
      <li>Fully Insured</li>
      <li>Obligation free quotes</li>
    </ul>
  </section>
</div>
</body>
</html>
```